Willowmere Therapy (Endure - Renew - Flourish) - Double Sided Business Card

I would like a 2-sided business card. Front: Matte Black or Navy with Logo & Tagline. Back: Name, Address, Phone Number, Email, & Website (maybe would like to include a small map pin-pointing location); Prefer front to be a gold/silver foil (iridescent); Back prefer white or light colored background with lettering that is easy to read and simple

Target Market(s)

Individuals & Couples (13 y.o. - ALL Adults); High end clientele

Industry/Entity Type

Licensed Professional Counselor (Mental Health)

Contact Information for Business Card

Name: Willowmere Therapy; Tagline: Endure - Renew - Flourish; Address: 3175 W. Calder Ave., Suite 842, Fort Worth, TX 76142; Phone: (214) 738-2956; Website: www.WillowmereTherapy.example

Font styles to use
Serif

Requirements
Must have
• Logo on Front (Large) prefer gold/silver foil on a matte dark color (i.e. black, navy, etc.); Back of Card: All other relevant information

```html
<!DOCTYPE html>
<html lang="en">
<head>
<meta charset="utf-8">
<title>Willowmere Therapy – Business Card</title>
<link rel="stylesheet" href="https://fonts.googleapis.com/css2?family=Cinzel:wght@500&family=Lato:wght@400&display=swap">
<style>
  :root {
    --navy: #050a24;
    --gold: #d4b35c;
    --silver: #8a8c91;
    --ink: #15182a;
    --paper: #ffffff;
    --backdrop: #e9e7e3;
  }
  * { box-sizing: border-box; margin: 0; padding: 0; }
  html, body { width: 1200px; height: 900px; overflow: hidden; }
  body {
    background: var(--backdrop);
    font-family: "Lato", sans-serif;
    position: relative;
  }
  .card {
    position: absolute;
    left: 250px;
    width: 700px;
    height: 400px;
    overflow: hidden;
    box-shadow: 0 6px 18px rgba(0,0,0,0.18);
  }
  .card--front { top: 40px; background: var(--navy); }
  .card--back { top: 470px; background: var(--paper); }

  /* Front */
  .front-lockup {
    position: absolute;
    inset: 0;
    display: flex;
    flex-direction: column;
    align-items: center;
    justify-content: center;
    gap: 18px;
  }
  .brand-dot {
    width: 74px;
    height: 74px;
    border-radius: 50%;
    border: 5px solid var(--silver);
  }
  .brand-name {
    font-family: "Cinzel", serif;
    font-weight: 500;
    color: var(--gold);
    font-size: 44px;
    letter-spacing: 2px;
    line-height: 1;
  }
  .tagline {
    font-family: "Cinzel", serif;
    font-weight: 500;
    color: var(--gold);
    font-size: 15px;
    letter-spacing: 2px;
    text-transform: uppercase;
  }

  /* Back */
  .back-wave { position: absolute; inset: 0; width: 700px; height: 400px; }
  .person { position: absolute; left: 58px; top: 62px; }
  .person__name {
    font-family: "Cinzel", serif;
    font-weight: 500;
    font-size: 31px;
    color: var(--gold);
    letter-spacing: 1px;
    line-height: 1;
  }
  .person__title { font-size: 18px; color: var(--ink); margin-top: 4px; }

  .contact { position: absolute; left: 58px; top: 158px; color: var(--ink); font-size: 17px; }
  .contact__row { display: flex; align-items: center; gap: 10px; height: 26px; }
  .contact__icon { width: 20px; height: 20px; flex: none; }
  .contact__address { margin-top: 22px; line-height: 1.35; padding-left: 30px; }

  .back-lockup {
    position: absolute;
    right: 40px;
    top: 50px;
    width: 250px;
    display: flex;
    flex-direction: column;
    align-items: center;
    gap: 10px;
  }
  .back-lockup .brand-dot { width: 54px; height: 54px; border-width: 4px; }
  .back-lockup .brand-name { font-size: 22px; letter-spacing: 1px; }
  .back-lockup .tagline { font-size: 10px; letter-spacing: 1.5px; }

  .website {
    position: absolute;
    right: 36px;
    bottom: 34px;
    color: var(--paper);
    font-size: 16px;
    letter-spacing: 0.3px;
  }
</style>
</head>
<body>

  <section class="card card--front" aria-label="Card front">
    <div class="front-lockup">
      <span class="brand-dot" aria-hidden="true"></span>
      <h1 class="brand-name">Willowmere Therapy</h1>
      <p class="tagline">Endure - Renew - Flourish</p>
    </div>
  </section>

  <section class="card card--back" aria-label="Card back">
    <svg class="back-wave" viewBox="0 0 700 400" aria-hidden="true">
      <path d="M0,356 C250,362 470,300 560,238 C610,204 660,172 700,158 V400 H0 Z" fill="var(--navy)"/>
      <path d="M0,322 C170,328 330,300 470,228 C350,312 190,346 0,346 Z" fill="var(--gold)"/>
    </svg>

    <div class="person">
      <h2 class="person__name">Daniel Harper</h2>
      <p class="person__title">Managing Director</p>
    </div>

    <div class="contact">
      <div class="contact__row">
        <svg class="contact__icon" viewBox="0 0 24 24" aria-hidden="true">
          <path d="M6.6 10.8a15.1 15.1 0 0 0 6.6 6.6l2.2-2.2a1 1 0 0 1 1-.25 11.4 11.4 0 0 0 3.6.57 1 1 0 0 1 1 1V20a1 1 0 0 1-1 1A17 17 0 0 1 3 4a1 1 0 0 1 1-1h3.5a1 1 0 0 1 1 1c0 1.25.2 2.45.57 3.57a1 1 0 0 1-.25 1Z" fill="var(--gold)"/>
        </svg>
        <span>(214) 738-2956</span>
      </div>
      <div class="contact__row">
        <svg class="contact__icon" viewBox="0 0 24 24" aria-hidden="true">
          <rect x="2" y="5" width="20" height="14" fill="var(--gold)"/>
          <path d="M2 5l10 8 10-8" fill="none" stroke="var(--paper)" stroke-width="1.6"/>
        </svg>
        <span>info@WillowmereTherapy.example</span>
      </div>
      <p class="contact__address">3175 W. Calder Ave., Suite 842<br>Fort Worth, TX 76142</p>
    </div>

    <div class="back-lockup">
      <span class="brand-dot" aria-hidden="true"></span>
      <p class="brand-name">Willowmere Therapy</p>
      <p class="tagline">Endure - Renew - Flourish</p>
    </div>

    <p class="website">www.WillowmereTherapy.example</p>
  </section>

</body>
</html>
```